Landscape design build company door flyer

I would like this flyer to convey a high-level of professionalism for a company that is excellent with communication with their clients as well as a company that does incredible installations

Went on vacation/holiday

```html
<!DOCTYPE html>
<html lang="en">
<head>
<meta charset="utf-8">
<title>Cedarline Builders – Outdoor Living Door Flyer</title>
<link rel="stylesheet" href="https://fonts.googleapis.com/css2?family=Great+Vibes&family=Montserrat:wght@400;500;600;700;800&display=swap">
<style>
  :root {
    --page-bg: #f2f2f2;
    --gap-white: #ffffff;
    --brand-yellow: #f9b81b;
    --charcoal: #2b2b2b;
    --charcoal-deep: #222324;
    --map-tone: #313234;
    --teal-tab: #16313d;
    --ink: #1f1f1f;
    --white: #ffffff;
  }
  * { box-sizing: border-box; margin: 0; padding: 0; }
  html, body {
    width: 1200px; height: 3112px; overflow: hidden;
    background: var(--page-bg);
    font-family: "Montserrat", sans-serif;
  }
  .flyer {
    position: absolute; left: 60px; top: 1139px;
    width: 1080px; height: 834px;
    background: var(--gap-white);
    box-shadow: 0 12px 40px rgba(0,0,0,.18);
    overflow: hidden;
  }
  .panel { position: absolute; }

  /* hero */
  .hero {
    left: 0; top: 0; width: 586px; height: 515px;
    background: linear-gradient(180deg, #0f1a24 0%, #15232d 42%, #1d3a2a 55%, #2b86ad 72%, #cfe3ec 100%);
  }
  .hero-headline {
    position: absolute; left: 0; top: 22px; width: 586px;
    text-align: center; color: var(--white);
  }
  .hero-script {
    font-family: "Great Vibes", cursive;
    font-size: 62px; line-height: 1; margin-left: 40px;
  }
  .hero-title {
    font-weight: 800; color: var(--brand-yellow);
    font-size: 60px; line-height: 1; letter-spacing: 0.5px; margin-top: -6px;
  }
  .hero-sub {
    font-weight: 500; font-size: 22px; letter-spacing: 6px; margin-top: 8px;
  }
  .services-tab {
    position: absolute; left: 0; bottom: 0; width: 0; height: 0;
  }
  .services-tab svg { position: absolute; left: 0; bottom: 0; }
  .services-label {
    position: absolute; left: 34px; bottom: 6px;
    color: var(--white); font-weight: 600; font-size: 32px; letter-spacing: .5px;
    white-space: nowrap;
  }

  .photo-firepit {
    left: 598px; top: 0; width: 237px; height: 260px;
    background: linear-gradient(180deg, #6f8fa8 0%, #3f5a36 35%, #7a5a44 60%, #8d6f5e 100%);
  }
  .photo-wall {
    left: 598px; top: 272px; width: 482px; height: 243px;
    background: linear-gradient(180deg, #c9cac6 0%, #a8a9a4 40%, #6d6a62 58%, #b3622a 78%, #8c4a1f 100%);
  }

  /* offer */
  .offer {
    left: 848px; top: 0; width: 232px; height: 260px;
    background: var(--charcoal-deep);
    color: var(--white); text-align: center;
    display: flex; flex-direction: column; justify-content: center; align-items: center;
  }
  .offer-get { font-size: 25px; font-weight: 500; }
  .offer-amount { display: flex; align-items: flex-start; color: var(--brand-yellow); margin: 2px 0 6px; }
  .offer-number { font-size: 72px; font-weight: 800; line-height: .9; }
  .offer-unit { display: flex; flex-direction: column; font-weight: 700; line-height: 1; text-align: left; margin-left: 2px; padding-top: 6px; }
  .offer-unit .pct { font-size: 30px; }
  .offer-unit .off { font-size: 22px; }
  .offer-project { font-size: 17px; font-weight: 500; }

  /* services band */
  .service-band {
    left: 0; top: 515px; width: 1080px; height: 104px;
    background: var(--brand-yellow);
    display: flex; align-items: center; justify-content: space-between;
    padding: 0 24px 0 26px;
  }
  .service-item {
    display: flex; align-items: flex-start; gap: 10px;
    color: var(--ink); font-size: 25px; font-weight: 500; line-height: 1.1;
    white-space: nowrap;
  }
  .service-item svg { flex: none; margin-top: 4px; }

  /* contact footer */
  .footer {
    left: 0; top: 619px; width: 1080px; height: 215px;
    background: var(--charcoal);
  }
  .brand-name {
    position: absolute; left: 34px; top: 52px; width: 290px;
    display: flex; flex-direction: column; align-items: center; gap: 22px;
    color: var(--white); font-weight: 600; font-size: 21px; letter-spacing: 1px;
    white-space: nowrap;
  }
  .brand-name .brand-square { width: 50px; height: 50px; background: var(--white); }

  .contact-cta {
    position: absolute; left: 398px; top: 34px;
    color: var(--brand-yellow); font-weight: 600; font-size: 17px; white-space: nowrap;
  }
  .contact-row {
    position: absolute; left: 365px;
    display: flex; align-items: center; gap: 14px;
    color: var(--white); white-space: nowrap;
  }
  .contact-phone { top: 58px; font-weight: 700; font-size: 29px; }
  .contact-web { top: 104px; font-size: 17px; letter-spacing: 2px; }
  .estimate-button {
    position: absolute; left: 363px; top: 144px; width: 262px;
    border: 2px solid var(--brand-yellow); border-radius: 4px;
    padding: 7px 0; text-align: center;
    color: var(--white); font-size: 12px; font-weight: 600; letter-spacing: 2px;
    white-space: nowrap;
  }
  .areas {
    position: absolute; left: 702px; top: 56px; width: 118px;
    color: var(--brand-yellow); font-size: 12px; line-height: 1.25; font-weight: 500;
  }
  .license { color: var(--white); font-size: 9px; margin-top: 14px; line-height: 1.3; }
  .service-map {
    position: absolute; left: 830px; top: 0; width: 250px; height: 215px;
    background: radial-gradient(ellipse at 50% 50%, #38393b 0%, var(--map-tone) 70%);
  }
</style>
</head>
<body>
  <main class="flyer">
    <section class="panel hero">
      <div class="panel hero" role="img" aria-label="Night view of a lit backyard pool with stone deck, lamp posts and a hedge"></div>
      <div class="hero-headline">
        <div class="hero-script">Let's Create</div>
        <div class="hero-title">YOUR DREAM</div>
        <div class="hero-sub">OUTDOOR LIVING SPACES</div>
      </div>
      <div class="services-tab">
        <svg width="276" height="47" viewBox="0 0 276 47"><polygon points="0,0 236,0 276,47 0,47" fill="#16313d"/></svg>
        <span class="services-label">SERVICES</span>
      </div>
    </section>

    <div class="panel photo-firepit" role="img" aria-label="Stone fire pit burning on a paver patio with curved seating wall and trees"></div>

    <aside class="panel offer">
      <div class="offer-get">Get</div>
      <div class="offer-amount">
        <span class="offer-number">10</span>
        <span class="offer-unit"><span class="pct">%</span><span class="off">OFF</span></span>
      </div>
      <div class="offer-project">OUR PROJECT</div>
    </aside>

    <div class="panel photo-wall" role="img" aria-label="Stone retaining wall with slate patio and warm wooden deck"></div>

    <section class="panel service-band">
      <div class="service-item"><svg width="22" height="20" viewBox="0 0 22 20"><path d="M2 11 L8 17 L20 3" fill="none" stroke="#fff" stroke-width="4" stroke-linecap="round"/><path d="M2 11 L8 17 L20 3" fill="none" stroke="#1f1f1f" stroke-width="2" stroke-linecap="round"/></svg><span>Pools</span></div>
      <div class="service-item"><svg width="22" height="20" viewBox="0 0 22 20"><path d="M2 11 L8 17 L20 3" fill="none" stroke="#fff" stroke-width="4" stroke-linecap="round"/><path d="M2 11 L8 17 L20 3" fill="none" stroke="#1f1f1f" stroke-width="2" stroke-linecap="round"/></svg><span>Paver<br>Patios</span></div>
      <div class="service-item"><svg width="22" height="20" viewBox="0 0 22 20"><path d="M2 11 L8 17 L20 3" fill="none" stroke="#fff" stroke-width="4" stroke-linecap="round"/><path d="M2 11 L8 17 L20 3" fill="none" stroke="#1f1f1f" stroke-width="2" stroke-linecap="round"/></svg><span>Decks &amp;<br>Railings</span></div>
      <div class="service-item"><svg width="22" height="20" viewBox="0 0 22 20"><path d="M2 11 L8 17 L20 3" fill="none" stroke="#fff" stroke-width="4" stroke-linecap="round"/><path d="M2 11 L8 17 L20 3" fill="none" stroke="#1f1f1f" stroke-width="2" stroke-linecap="round"/></svg><span>Firepits &amp;<br>Fireplaces</span></div>
      <div class="service-item"><svg width="22" height="20" viewBox="0 0 22 20"><path d="M2 11 L8 17 L20 3" fill="none" stroke="#fff" stroke-width="4" stroke-linecap="round"/><path d="M2 11 L8 17 L20 3" fill="none" stroke="#1f1f1f" stroke-width="2" stroke-linecap="round"/></svg><span>Retaining<br>Walls</span></div>
      <div class="service-item"><svg width="22" height="20" viewBox="0 0 22 20"><path d="M2 11 L8 17 L20 3" fill="none" stroke="#fff" stroke-width="4" stroke-linecap="round"/><path d="M2 11 L8 17 L20 3" fill="none" stroke="#1f1f1f" stroke-width="2" stroke-linecap="round"/></svg><span>Paver<br>Driveways</span></div>
    </section>

    <footer class="panel footer">
      <div class="brand-name"><span class="brand-square"></span><span>CEDARLINE BUILDERS</span></div>

      <div class="contact-cta">CALL US NOW!</div>
      <div class="contact-row contact-phone">
        <svg width="18" height="18" viewBox="0 0 24 24"><path d="M6.6 10.8a15.1 15.1 0 0 0 6.6 6.6l2.2-2.2a1 1 0 0 1 1-.25 11.4 11.4 0 0 0 3.6.57 1 1 0 0 1 1 1V20a1 1 0 0 1-1 1A17 17 0 0 1 3 4a1 1 0 0 1 1-1h3.5a1 1 0 0 1 1 1c0 1.25.2 2.45.57 3.57a1 1 0 0 1-.25 1z" fill="#f9b81b"/></svg>
        <span>(206) 555-0148</span>
      </div>
      <div class="contact-row contact-web">
        <svg width="18" height="18" viewBox="0 0 24 24"><rect x="1" y="1" width="22" height="22" rx="5" fill="#f9b81b"/><circle cx="12" cy="12" r="6.5" fill="none" stroke="#2b2b2b" stroke-width="1.6"/><path d="M5.5 12h13M12 5.5c-3 3.5-3 9.5 0 13M12 5.5c3 3.5 3 9.5 0 13" fill="none" stroke="#2b2b2b" stroke-width="1.4"/></svg>
        <span>cedarlinebuilders.com</span>
      </div>
      <div class="estimate-button">GET A FAST FREE ESTIMATE</div>

      <div class="areas">
        YOUR AREAS<br>WE SERVE<br>OUTDOOR<br>LIVING<br>CONTRACTOR
        <div class="license">License #<br>CEDARLB902KT</div>
      </div>

      <div class="service-map" role="img" aria-label="Dark map of the service area with location pins on nearby cities"></div>
    </footer>
  </main>
</body>
</html>
```